Vorlage für ein Workbook
Zielgruppe
Coaching und Beratung
Aufgabenstellung
Es soll eine Vorlage für ein Workbook erstellt werden, das ich dann selbst mit Inhalten füllen kann.. evtl. mit Canvas oder wie auch immer....
Es ist ein 12 Wochenkurs, d.h. ich brauche 1 Titelseite für jede Woche, die ich dann paste und copy machen kann und beschriften kann, sowie eine Vorlage für die einzelnen Seiten des Workbooks. Das Workbook in pdf Format muss auch online ausgefüllt werden können.
Design angepasst an Landingpage

```html
<!DOCTYPE html>
<html lang="de">
<head>
<meta charset="utf-8">
<title>Workbook Vorlage – Seitenübersicht</title>
<link rel="stylesheet" href="https://fonts.googleapis.com/css2?family=Cinzel:wght@400&family=Oswald:wght@300&display=swap">
<style>
  :root {
    --bg-top: #5f6a8b;
    --bg-bottom: #aab0c8;
    --paper: #ffffff;
    --line: #c3beb6;
    --title: #c6c1ba;
    --ink: #1f1f1f;
    --sub: #3a3a3a;
    --leaf-soft: #efece8;
  }
  * { margin: 0; padding: 0; box-sizing: border-box; }
  html, body { width: 848px; height: 1200px; overflow: hidden; }
  body {
    position: relative;
    background: linear-gradient(200deg, var(--bg-top) 0%, #8891ae 50%, var(--bg-bottom) 100%);
    font-family: "Oswald", "Arial Narrow", sans-serif;
  }
  .page {
    position: absolute;
    width: 397px; height: 562px;
    background: var(--paper);
    overflow: hidden;
  }
  .page--week-a { left: 15px; top: 27px; }
  .page--week-b { left: 434px; top: 27px; }
  .page--week-c { left: 15px; top: 610px; }
  .page--content { left: 436px; top: 610px; }
  .page__inner {
    position: absolute; left: 0; top: 0;
    width: 595px; height: 843px;
    transform: scale(0.6672);
    transform-origin: 0 0;
  }
  .page__lines {
    position: absolute; inset: 0; width: 595px; height: 843px;
    fill: none; stroke: var(--line);
  }
  .stroke-bold { stroke-width: 3; }
  .stroke-fine { stroke-width: 1.2; }
  .blob { stroke: var(--line); fill: none; }
  .foliage {
    position: absolute;
    background: radial-gradient(ellipse at center, var(--leaf-soft) 0%, rgba(239,236,232,0.6) 55%, rgba(255,255,255,0) 75%);
  }
  .heading {
    position: absolute;
    text-align: center;
    font-family: "Cinzel", "Trajan Pro", serif;
  }
  .heading__title {
    font-size: 48px; line-height: 1;
    color: var(--title);
    letter-spacing: 1px;
  }
  .heading__sub {
    margin-top: 8px;
    font-size: 12.5px; line-height: 15px;
    color: var(--sub);
    letter-spacing: 0.3px;
  }
  .note {
    position: absolute;
    font-size: 16px; line-height: 22.7px;
    color: var(--ink);
    font-weight: 300;
    white-space: nowrap;
  }
  .note--list { list-style: none; }
</style>
</head>
<body>

<svg width="0" height="0" style="position:absolute" aria-hidden="true">
  <defs>
    <symbol id="bubble" viewBox="0 0 100 100" preserveAspectRatio="none" overflow="visible">
      <path vector-effect="non-scaling-stroke" stroke-width="3" d="M8,30 C14,8 40,12 60,8 C82,4 98,18 96,45 C94,75 88,96 55,92 C30,89 6,95 4,62 C3,48 4,40 8,30 Z"/>
      <path vector-effect="non-scaling-stroke" stroke-width="1.2" d="M4,45 C2,16 30,2 55,10 C75,15 100,5 99,38 C98,70 96,99 62,96 C40,94 12,101 6,70 C5,60 4,52 4,45 Z"/>
    </symbol>
  </defs>
</svg>

<!-- Wochen-Titelseite A -->
<section class="page page--week-a">
  <div class="page__inner">
    <svg class="page__lines" viewBox="0 0 595 843" aria-hidden="true">
      <path class="stroke-bold" d="M0,212 C90,245 130,300 130,380 C130,470 200,490 330,495 C450,500 560,540 595,590"/>
      <path class="stroke-fine" d="M0,308 C80,330 110,380 115,430 C125,520 200,545 320,545 C450,545 540,560 595,575"/>
      <use class="blob" href="#bubble" x="90" y="58" width="280" height="198"/>
      <use class="blob" href="#bubble" x="185" y="590" width="360" height="210"/>
    </svg>
    <div class="foliage" role="img" aria-label="Zweig mit Blättern und Beeren als Linienzeichnung" style="left:370px;top:0;width:225px;height:260px"></div>
    <div class="foliage" role="img" aria-label="Zweig mit Blättern und Beeren als Linienzeichnung" style="left:0;top:612px;width:205px;height:231px"></div>
    <p class="note" style="left:123px;top:110px">Lorem ipsum dolor sit amet, consecte-<br>tuer adipiscing elit, sed diam nonum-<br>my nibh euismod tincidunt ut laoreet<br>dolore magna aliquamLorem ipsum</p>
    <div class="heading" style="left:190px;top:315px;width:340px">
      <div class="heading__title">Lorem Ipsum</div>
      <div class="heading__sub">LOREM IPSUM DOLOR SIT AMET, CONSECTETUER ADIPISCING ELIT, SED DIAM NONUMMY NIBH EUIS-MOD TINCIDUNT UT LAOREET DOLORE MAGNA ALIQUAM</div>
    </div>
    <p class="note" style="left:228px;top:650px">Lorem ipsum dolor sit amet, consectetuer adipis-<br>cing elit, sed diam nonummy nibh euismod<br>&nbsp;tincidunt ut laoreet dolore magna aliquamLorem<br>&nbsp;ipsum dolor sit amet, consecte-</p>
  </div>
</section>

<!-- Wochen-Titelseite B -->
<section class="page page--week-b">
  <div class="page__inner">
    <svg class="page__lines" viewBox="0 0 595 843" aria-hidden="true">
      <path class="stroke-bold" d="M0,158 C150,140 230,200 270,260 C310,320 360,345 420,320 C480,290 540,240 595,275"/>
      <path class="stroke-fine" d="M0,200 C140,190 220,230 250,280 C280,330 320,360 380,300 C430,250 520,230 595,265"/>
      <path class="stroke-bold" d="M0,652 C80,642 130,650 140,700 C148,750 138,800 135,843"/>
      <path class="stroke-fine" d="M0,555 C120,580 170,600 185,650 C195,720 170,790 190,843"/>
      <path class="stroke-fine" d="M0,700 C40,690 90,690 115,700 C135,710 130,780 120,843"/>
      <use class="blob" href="#bubble" x="25" y="358" width="400" height="198"/>
    </svg>
    <div class="foliage" role="img" aria-label="Zweig mit großen Blättern als Linienzeichnung" style="left:285px;top:465px;width:310px;height:378px"></div>
    <div class="heading" style="left:150px;top:75px;width:340px">
      <div class="heading__title">Lorem Ipsum</div>
      <div class="heading__sub">LOREM IPSUM DOLOR SIT AMET, CONSECTETUER ADIPISCING ELIT, SED DIAM NONUMMY NIBH EUIS-MOD TINCIDUNT UT LAOREET DOLORE MAGNA ALIQUAM</div>
    </div>
    <p class="note" style="left:66px;top:410px">Lorem ipsum dolor sit amet, consectetuer adipiscing elit,<br>sed diam nonummy nibh euismod tincidunt ut laoreet<br>dolore magna aliquamLorem ipsum dolor sit amet,<br>consectetuer adipiscing elit, sed diam nonummy nibh</p>
  </div>
</section>

<!-- Wochen-Titelseite C -->
<section class="page page--week-c">
  <div class="page__inner">
    <svg class="page__lines" viewBox="0 0 595 843" aria-hidden="true">
      <path class="stroke-fine" d="M412,0 C392,80 410,142 490,140 C560,138 540,200 570,240 C580,252 588,258 595,262"/>
      <path class="stroke-fine" d="M435,0 C420,60 440,112 520,120 C555,124 560,160 595,170"/>
      <path class="stroke-bold" d="M0,812 C100,780 200,680 235,560 C260,480 320,440 400,450 C480,460 550,410 595,400"/>
      <path class="stroke-fine" d="M20,843 C140,760 230,620 280,520 C330,440 420,420 595,440"/>
      <use class="blob" href="#bubble" x="40" y="50" width="330" height="195"/>
      <use class="blob" href="#bubble" x="275" y="555" width="275" height="200"/>
    </svg>
    <div class="foliage" role="img" aria-label="Zweig mit großen Blättern als Linienzeichnung" style="left:0;top:435px;width:200px;height:280px"></div>
    <p class="note" style="left:82px;top:106px">Lorem ipsum dolor sit amet, consectetuer<br>adipiscing elit, sed diam nonummy nibh<br>&nbsp;euismod tincidunt ut laoreet dolore magna<br>&nbsp;ali-</p>
    <div class="heading" style="left:145px;top:295px;width:340px">
      <div class="heading__title">Lorem Ipsum</div>
      <div class="heading__sub">LOREM IPSUM DOLOR SIT AMET, CONSECTETUER ADIPISCING ELIT, SED DIAM NONUMMY NIBH EUIS-MOD TINCIDUNT UT LAOREET DOLORE MAGNA ALIQUAM</div>
    </div>
    <p class="note" style="left:312px;top:612px">Lorem ipsum dolor sit amet, consecte-<br>tuer adipiscing elit, sed diam nonum-<br>my nibh euismod tincidunt ut laoreet<br>dolore magna aliquamLorem ipsum</p>
  </div>
</section>

<!-- Inhaltsseite -->
<section class="page page--content">
  <div class="page__inner">
    <svg class="page__lines" viewBox="0 0 595 843" aria-hidden="true">
      <path class="stroke-bold" d="M175,0 C200,120 260,200 360,230 C460,260 520,300 540,380 C560,460 545,600 595,640"/>
      <path class="stroke-fine" d="M195,0 C220,110 280,190 380,220 C480,250 560,300 570,420 C575,520 560,600 595,620"/>
      <use class="blob" href="#bubble" x="275" y="30" width="275" height="165"/>
      <use class="blob" href="#bubble" x="45" y="270" width="400" height="300"/>
      <use class="blob" href="#bubble" x="50" y="610" width="275" height="160"/>
    </svg>
    <div class="foliage" role="img" aria-label="Zweig mit Blättern und Beeren als Linienzeichnung" style="left:0;top:25px;width:205px;height:195px"></div>
    <div class="foliage" role="img" aria-label="Zweig mit Blättern und Beeren als Linienzeichnung" style="left:340px;top:570px;width:255px;height:273px"></div>
    <ul class="note note--list" style="left:315px;top:60px">
      <li>- Lorem ipsum dolor sit amet,</li>
      <li>- consectetuer adipiscing elit,</li>
      <li>- sed diam nonummy nibh euismod<br>tincidunt ut</li>
      <li>- laoreet dolore magna</li>
    </ul>
    <p class="note" style="left:96px;top:336px">Lorem ipsum dolor sit amet, consectetuer adipiscing elit,<br>sed diam nonummy nibh euismod tincidunt ut laoreet<br>dolore magna aliquamLorem ipsum dolor sit amet, consec-<br>tetuer adipiscing elit, sed diam nonummy nibh euismod<br>tincidunt ut laoreet dolore magna aliquam erat volutpat. Ut<br>wisi enim ad Lorem ipsum dolor sit amet, consectetuer<br>adipiscing elit, sed diam nonummy nibh euismod tincidunt<br>ut laoreet dolore magna aliquam erat volutpat. Ut wisi</p>
    <ul class="note note--list" style="left:88px;top:660px">
      <li>- Lorem ipsum dolor sit amet,</li>
      <li>- consectetuer adipiscing elit,</li>
      <li>- sed diam nonummy nibh euismod<br>tincidunt ut</li>
    </ul>
  </div>
</section>

</body>
</html>
```